Design Workout/Fitness Mobile App

Create a design for a mobile workout out a mobile app called Brisko Routine. This workout app is very similar to Tally Stretch Session. Please download or search for the Tally Stretch Session in the Fable Market to get an idea, I will also include a link below.

App Description: http://lnkwrap.example/q8Tz4Rm

The main difference between Brisko Routine and Tally Stretch Session is that Brisko Routines are 8 Minutes instead of 7 Minute and Brisko Routine are created/demonstrated by a real human being instead of an animated video.
Please read the referenced Quillet Sheet and install or go through the Tally Stretch app. I am open to any design color. The app is targetted at people who need a quick workout but do not have a lot of time

Example (Tally Stretch Session): http://lnkwrap.example/v3KpX7n

Target Market(s)

Busy working adults

Industry/Entity Type

Fitness

Colors

Designer to choose colors to be used in the design.

Requirements
Must have
• This design is for at least three screens
• The main screen showing a list of the types of exercises such as lower body, abs, etc
• The workout screen showing the video
• A calendar showing the number of days user worked.
Nice to have
• Make the designs close to the Tally-stretch session with different look and feel

```html
<!DOCTYPE html>
<html lang="en">
<head>
<meta charset="utf-8">
<title>Brisko Routine – App Screens</title>
<link href="https://fonts.googleapis.com/css2?family=Open+Sans:wght@400;600;700&family=Montserrat:wght@400;600;700&display=swap" rel="stylesheet">
<style>
  :root{
    --page:#efefef;
    --ink:#222222;
    --dark:#2b2b2b;
    --dark-2:#3a3a3a;
    --yellow:#f6c21c;
    --muted:#b8b8b8;
    --text-soft:#666666;
    --line:#e6e6e6;
    --band:#f3f3f3;
    --white:#ffffff;
  }
  *{box-sizing:border-box;margin:0;padding:0}
  html,body{width:1200px;height:662px;overflow:hidden;background:var(--page);font-family:"Open Sans",Arial,sans-serif;color:var(--ink)}
  .board{position:relative;width:1200px;height:662px}
  .step-no{position:absolute;top:48px;width:40px;text-align:center;font:700 19px "Open Sans",Arial,sans-serif;color:var(--ink)}
  .screen{position:absolute;top:96px;width:224px;height:486px;background:var(--white);border-radius:24px;overflow:hidden;box-shadow:0 2px 10px rgba(0,0,0,.06)}
  .status{position:absolute;top:0;left:0;right:0;height:26px;display:flex;align-items:center;justify-content:space-between;padding:0 14px 0 18px;font:600 10px "Open Sans",Arial,sans-serif;color:var(--white);z-index:3}
  .status svg{display:block}
  .home-bar{position:absolute;bottom:8px;left:50%;width:80px;height:3px;margin-left:-40px;border-radius:2px;background:#c9c9c9;z-index:4}
  .appbar{position:absolute;top:0;left:0;right:0;height:62px;background:var(--dark)}
  .appbar-title{position:absolute;top:37px;left:0;right:0;text-align:center;font:400 13px "Open Sans",Arial,sans-serif;color:var(--white)}
  .appbar-icon{position:absolute;top:38px}
  .tabs{position:absolute;top:62px;left:0;right:0;height:28px;display:flex;background:var(--white)}
  .tab{flex:1;text-align:center;font:400 11px "Open Sans",Arial,sans-serif;color:var(--muted);padding-top:6px;position:relative}
  .tab.is-active{color:var(--ink);font-weight:600}
  .tab.is-active::after{content:"";position:absolute;left:22px;right:22px;bottom:1px;height:2px;background:var(--yellow)}

  /* Splash */
  .splash{left:54px;background:var(--dark)}
  .splash-photo{position:absolute;inset:0;background:radial-gradient(ellipse at 52% 32%,#5a5a5a 0%,#404040 35%,#2e2e2e 70%)}
  .brand{position:absolute;top:232px;left:0;right:0;text-align:center;font:700 24px "Montserrat",Arial,sans-serif;color:var(--white);letter-spacing:1px;line-height:1.05;text-transform:uppercase}
  .brand-dot{display:inline-block;width:10px;height:10px;border-radius:50%;background:var(--yellow);margin-right:6px;vertical-align:middle}
  .splash .home-bar{background:#d0d0d0}

  /* Dashboard list */
  .dash{left:344px}
  .cards{position:absolute;top:94px;left:2px;right:2px}
  .card{position:relative;height:112px;margin-bottom:3px;overflow:hidden}
  .card-photo{position:absolute;inset:0}
  .card-abs .card-photo{background:linear-gradient(160deg,#8a5a43,#5e3a2a 55%,#3b261c)}
  .card-leg .card-photo{background:linear-gradient(160deg,#3b3b3b,#202020 60%,#151515)}
  .card-stretch .card-photo{background:linear-gradient(160deg,#7b8491,#55606c 60%,#3b434c)}
  .card-more{height:50px}
  .card-more .card-photo{background:linear-gradient(90deg,#6e4a2a,#b07a43 50%,#6b4528)}
  .card-shade{position:absolute;left:0;right:0;bottom:0;height:42px;background:rgba(40,40,40,.72)}
  .card-title{position:absolute;left:14px;bottom:18px;font:700 11.5px "Open Sans",Arial,sans-serif;color:var(--yellow)}
  .card-sub{position:absolute;left:14px;right:8px;bottom:7px;font:600 6.5px "Open Sans",Arial,sans-serif;color:var(--white);white-space:nowrap;overflow:hidden}

  /* Workout detail */
  .workout{left:629px}
  .exercise-title{position:absolute;left:12px;font:600 11px "Open Sans",Arial,sans-serif;color:var(--ink)}
  .video{position:absolute;left:2px;right:2px;height:112px}
  .video-one{top:94px;background:linear-gradient(180deg,#d9cfc1,#c8b9a4 60%,#a48a70)}
  .video-two{top:330px;background:linear-gradient(180deg,#3c3a44,#2f3b52 55%,#2d5878)}
  .video-play{position:absolute;left:50%;top:50%;margin:-13px 0 0 -13px}
  .copy{position:absolute;left:12px;right:10px;top:216px;font:400 8.2px/1.2 "Open Sans",Arial,sans-serif;color:var(--text-soft)}
  .copy p+p{margin-top:8px}
  .copy-tail{position:absolute;left:12px;top:455px;font:400 8.2px "Open Sans",Arial,sans-serif;color:var(--text-soft)}
  .fab{position:absolute;left:172px;top:409px;width:42px;height:42px;border-radius:50%;background:var(--yellow);display:flex;align-items:center;justify-content:center}

  /* Calendar */
  .calendar{left:918px}
  .month-bar{position:absolute;top:90px;left:0;right:0;height:30px;background:var(--band);display:flex;align-items:center;justify-content:space-between;padding:0 18px}
  .month-name{font:400 13px "Montserrat",Arial,sans-serif;letter-spacing:3px;color:var(--ink)}
  .grid{position:absolute;top:122px;left:8px;right:8px;display:grid;grid-template-columns:repeat(7,1fr);grid-auto-rows:29.5px;text-align:center}
  .dow{font:600 7px "Open Sans",Arial,sans-serif;color:var(--ink);letter-spacing:1px;line-height:19px;height:19px}
  .day{position:relative;font:400 9.5px/29.5px "Montserrat",Arial,sans-serif;color:var(--ink);letter-spacing:1px}
  .day.is-out{color:var(--muted)}
  .day.has-dot::after{content:"";position:absolute;left:50%;bottom:3px;width:2px;height:2px;margin-left:-1px;border-radius:50%;background:#2a9fd6}
  .day.is-today span,.day.is-selected span{display:inline-block;width:27px;height:27px;border-radius:50%;line-height:27px;margin-top:1px}
  .day.is-today span{border:1.5px solid var(--yellow);line-height:24px}
  .day.is-selected span{background:var(--yellow);border:1px solid #e0a800}
  .stats{position:absolute;top:296px;left:0;right:0;height:68px;border-top:1px solid var(--line);border-bottom:1px solid var(--line);display:flex}
  .stat{flex:1;text-align:center;padding-top:9px;position:relative}
  .stat+.stat::before{content:"";position:absolute;left:0;top:14px;bottom:14px;width:1px;background:var(--line)}
  .stat-value{font:400 17px "Montserrat",Arial,sans-serif;color:#444}
  .stat-label{font:600 6px/1.25 "Open Sans",Arial,sans-serif;color:#555;text-transform:uppercase;margin-top:3px}
  .profile{position:absolute;top:364px;left:0;right:0;height:84px}
  .avatar{position:absolute;left:14px;top:22px;width:42px;height:42px;border-radius:50%;background:linear-gradient(160deg,#c9d3de,#8fa3b8)}
  .weight{position:absolute;left:64px;top:36px;font:400 15px "Montserrat",Arial,sans-serif;color:var(--ink)}
  .weight small{font-size:7px;font-weight:600}
  .profile-divider{position:absolute;left:122px;top:14px;bottom:4px;width:1px;background:var(--line)}
  .metrics{position:absolute;left:130px;right:10px;top:14px}
  .metric{display:flex;align-items:baseline;height:21px}
  .metric-value{width:46px;text-align:right;font:400 14px "Montserrat",Arial,sans-serif;color:var(--ink);padding-right:8px}
  .metric:not(:first-child) .metric-value{text-align:center;padding-right:0;width:36px}
  .metric-label{flex:1;text-align:right;font:400 8px "Open Sans",Arial,sans-serif;color:#444}
</style>
</head>
<body>
<main class="board">

  <div class="step-no" style="left:148px">1</div>
  <div class="step-no" style="left:436px">2</div>
  <div class="step-no" style="left:716px">3</div>
  <div class="step-no" style="left:1002px">4</div>

  <!-- Screen 1: splash -->
  <section class="screen splash" aria-label="Splash screen">
    <div class="splash-photo" role="img" aria-label="Dimmed photo of a smiling trainer holding dumbbells"></div>
    <div class="status"><span>9:41</span>
      <svg width="46" height="10" viewBox="0 0 46 10"><g fill="#fff"><rect x="0" y="6" width="2" height="4"/><rect x="3" y="4" width="2" height="6"/><rect x="6" y="2" width="2" height="8"/><rect x="9" y="0" width="2" height="10"/><path d="M15 3a8 8 0 0 1 10 0l-1.2 1.3a6 6 0 0 0-7.6 0z M17.3 5.6a4.5 4.5 0 0 1 5.4 0L20 9z"/><rect x="29" y="1" width="15" height="8" rx="2" fill="none" stroke="#fff"/><rect x="30.5" y="2.5" width="12" height="5" rx="1"/></g></svg>
    </div>
    <div class="brand"><span class="brand-dot"></span>Brisko<br>Routine</div>
    <div class="home-bar"></div>
  </section>

  <!-- Screen 2: dashboard / workout list -->
  <section class="screen dash" aria-label="Dashboard workout list">
    <header class="appbar">
      <div class="appbar-title">Dashboard</div>
      <svg class="appbar-icon" style="right:12px" width="13" height="13" viewBox="0 0 13 13"><circle cx="5.3" cy="5.3" r="4.3" fill="none" stroke="#fff" stroke-width="1.4"/><path d="M8.5 8.5l3.6 3.6" stroke="#fff" stroke-width="1.4"/></svg>
    </header>
    <div class="status"><span>9:41</span>
      <svg width="46" height="10" viewBox="0 0 46 10"><g fill="#fff"><rect x="0" y="6" width="2" height="4"/><rect x="3" y="4" width="2" height="6"/><rect x="6" y="2" width="2" height="8"/><rect x="9" y="0" width="2" height="10"/><path d="M15 3a8 8 0 0 1 10 0l-1.2 1.3a6 6 0 0 0-7.6 0z M17.3 5.6a4.5 4.5 0 0 1 5.4 0L20 9z"/><rect x="29" y="1" width="15" height="8" rx="2" fill="none" stroke="#fff"/><rect x="30.5" y="2.5" width="12" height="5" rx="1"/></g></svg>
    </div>
    <nav class="tabs"><div class="tab is-active">Workout</div><div class="tab">Calendar</div></nav>
    <div class="cards">
      <article class="card card-abs">
        <div class="card-photo" role="img" aria-label="Close-up photo of toned abdominal muscles"></div>
        <div class="card-shade"></div>
        <div class="card-title">Abs Workout</div>
        <div class="card-sub">Do this quick circuit after cardio (or before the be...</div>
      </article>
      <article class="card card-leg">
        <div class="card-photo" role="img" aria-label="Photo of legs in training shoes mid-exercise"></div>
        <div class="card-shade"></div>
        <div class="card-title">Leg Workout</div>
        <div class="card-sub">Includes five workout programs to help you build m...</div>
      </article>
      <article class="card card-stretch">
        <div class="card-photo" role="img" aria-label="Photo of a woman stretching on a mat"></div>
        <div class="card-shade"></div>
        <div class="card-title">Sleepy Time Stretch</div>
        <div class="card-sub">Feel the afterburn all night long with a no-sweat, full-body workout</div>
      </article>
      <article class="card card-more">
        <div class="card-photo" role="img" aria-label="Photo of two people training together"></div>
      </article>
    </div>
    <div class="home-bar"></div>
  </section>

  <!-- Screen 3: workout detail -->
  <section class="screen workout" aria-label="Workout video screen">
    <header class="appbar">
      <svg class="appbar-icon" style="left:12px;top:39px" width="16" height="12" viewBox="0 0 16 12"><path d="M15 6H2M6.5 1.2L1.5 6l5 4.8" fill="none" stroke="#fff" stroke-width="1.5"/></svg>
      <div class="appbar-title">Workout</div>
    </header>
    <div class="status"><span>9:41</span>
      <svg width="46" height="10" viewBox="0 0 46 10"><g fill="#fff"><rect x="0" y="6" width="2" height="4"/><rect x="3" y="4" width="2" height="6"/><rect x="6" y="2" width="2" height="8"/><rect x="9" y="0" width="2" height="10"/><path d="M15 3a8 8 0 0 1 10 0l-1.2 1.3a6 6 0 0 0-7.6 0z M17.3 5.6a4.5 4.5 0 0 1 5.4 0L20 9z"/><rect x="29" y="1" width="15" height="8" rx="2" fill="none" stroke="#fff"/><rect x="30.5" y="2.5" width="12" height="5" rx="1"/></g></svg>
    </div>
    <div class="exercise-title" style="top:70px">1/15 Jumping Squats</div>
    <div class="video video-one" role="img" aria-label="Video still of a trainer demonstrating jumping squats in a studio">
      <svg class="video-play" width="26" height="26" viewBox="0 0 26 26"><circle cx="13" cy="13" r="11.5" fill="rgba(0,0,0,.25)" stroke="#fff" stroke-width="1.6"/><path d="M10.5 8.5l7 4.5-7 4.5z" fill="#fff"/></svg>
    </div>
    <div class="copy">
      <p>Before any fitness movement or event, you should always properly warm up.</p>
      <p>You want to start by getting your heart rate up by doing some type of rhythmic movement like jumping jacks or marching in place or light jog-ging to get your body ready for the upcoming activity.</p>
    </div>
    <div class="exercise-title" style="top:307px">2/15 Reverse Crunches</div>
    <div class="video video-two" role="img" aria-label="Video still of a woman doing reverse crunches on a mat">
      <svg class="video-play" width="26" height="26" viewBox="0 0 26 26"><circle cx="13" cy="13" r="11.5" fill="rgba(0,0,0,.25)" stroke="#fff" stroke-width="1.6"/><path d="M10.5 8.5l7 4.5-7 4.5z" fill="#fff"/></svg>
    </div>
    <div class="fab"><svg width="16" height="16" viewBox="0 0 16 16"><path d="M4 2l10 6-10 6z" fill="#222"/></svg></div>
    <div class="copy-tail">First, you're going to crunch forward and then</div>
    <div class="home-bar"></div>
  </section>

  <!-- Screen 4: calendar -->
  <section class="screen calendar" aria-label="Dashboard calendar">
    <header class="appbar">
      <div class="appbar-title">Dashboard</div>
      <svg class="appbar-icon" style="right:12px" width="13" height="13" viewBox="0 0 13 13"><circle cx="5.3" cy="5.3" r="4.3" fill="none" stroke="#fff" stroke-width="1.4"/><path d="M8.5 8.5l3.6 3.6" stroke="#fff" stroke-width="1.4"/></svg>
    </header>
    <div class="status"><span>9:41</span>
      <svg width="46" height="10" viewBox="0 0 46 10"><g fill="#fff"><rect x="0" y="6" width="2" height="4"/><rect x="3" y="4" width="2" height="6"/><rect x="6" y="2" width="2" height="8"/><rect x="9" y="0" width="2" height="10"/><path d="M15 3a8 8 0 0 1 10 0l-1.2 1.3a6 6 0 0 0-7.6 0z M17.3 5.6a4.5 4.5 0 0 1 5.4 0L20 9z"/><rect x="29" y="1" width="15" height="8" rx="2" fill="none" stroke="#fff"/><rect x="30.5" y="2.5" width="12" height="5" rx="1"/></g></svg>
    </div>
    <nav class="tabs"><div class="tab">Workout</div><div class="tab is-active">Calendar</div></nav>
    <div class="month-bar">
      <svg width="6" height="9" viewBox="0 0 6 9"><path d="M5 1L1.5 4.5 5 8" fill="none" stroke="#999" stroke-width="1.1"/></svg>
      <span class="month-name">AUGUST 2018</span>
      <svg width="6" height="9" viewBox="0 0 6 9"><path d="M1 1l3.5 3.5L1 8" fill="none" stroke="#999" stroke-width="1.1"/></svg>
    </div>
    <div class="grid">
      <div class="dow">Mo</div><div class="dow">Tu</div><div class="dow">We</div><div class="dow">Th</div><div class="dow">Fr</div><div class="dow">Sa</div><div class="dow">Su</div>
      <div class="day is-out">29</div><div class="day is-out">30</div><div class="day is-out">31</div><div class="day">1</div><div class="day has-dot">2</div><div class="day">3</div><div class="day">4</div>
      <div class="day">5</div><div class="day">6</div><div class="day">7</div><div class="day">8</div><div class="day">9</div><div class="day">10</div><div class="day">11</div>
      <div class="day">12</div><div class="day has-dot">13</div><div class="day">14</div><div class="day">15</div><div class="day">16</div><div class="day">17</div><div class="day is-today"><span>18</span></div>
      <div class="day">19</div><div class="day">20</div><div class="day">21</div><div class="day">22</div><div class="day is-selected"><span>23</span></div><div class="day">24</div><div class="day">25</div>
      <div class="day">26</div><div class="day">27</div><div class="day">28</div><div class="day">29</div><div class="day">30</div><div class="day">31</div><div class="day is-out">1</div>
    </div>
    <div class="stats">
      <div class="stat"><div class="stat-value">15</div><div class="stat-label">Max<br>Streak</div></div>
      <div class="stat"><div class="stat-value">9</div><div class="stat-label">Current<br>Streak</div></div>
      <div class="stat"><div class="stat-value">155</div><div class="stat-label">Total for the<br>last 30 days</div></div>
    </div>
    <div class="profile">
      <div class="avatar" role="img" aria-label="User profile photo"></div>
      <div class="weight">122 <small>LBS</small></div>
      <div class="profile-divider"></div>
      <div class="metrics">
        <div class="metric"><span class="metric-value">15.05</span><span class="metric-label">Duration</span></div>
        <div class="metric"><span class="metric-value">2</span><span class="metric-label">Pause</span></div>
        <div class="metric"><span class="metric-value">3</span><span class="metric-label">Repeat</span></div>
      </div>
    </div>
    <div class="home-bar"></div>
  </section>

</main>
</body>
</html>
```